Business Card - Business Consultancy

Newly Established Company, specializing in Business Consultancy, Human Resource Management, Talent Acquisition and Payroll Solutions.

We need a Business card design which portrays "elegance" and a very sleek yet business-like design. We would like a nice blue trimming (which goes well with the logo) to separate the content of the business card at the top. We would also like to see the design using the color silver either as a background or incorporated into it.

The final design should be a Business card which has colors matching the logo; a nice font; the above-mentioned specifics that adheres to the theme of "a stylish and professional business"

FYI: please do not have too fanciful designs.

Industry/Entity Type

Business Consultant

Contact Information for Business Card

Marcus Tellon
Business Development Director
Brightpath HR Consulting Private Limited
27 Wexford Lane, #05-03B
Harbourview Trade Tower
Singapore 061739
Mobile : (+65) 94386157
Email : mtellon@brightpathhr-advisory.com
Alternative : brightpathhradvisory@mailbox-example.com

Requirements
Must have
• Nice Blue Trimming matching Logo which separates content, see attached
• Design incorporates either a silver background or the use of the color silver
Should not have
• No Fanciful Designs
• No Childish Designs
• No Overly Complicated Designs

```html
<!DOCTYPE html>
<html lang="en">
<head>
<meta charset="utf-8">
<title>Brightpath HR Consulting — Business Card</title>
<link rel="stylesheet" href="https://fonts.googleapis.com/css2?family=Arimo:wght@400;700&family=Titillium+Web:wght@400;600&family=Montserrat:wght@600&display=swap">
<style>
  :root {
    --backdrop-light: #e4e4e4;
    --backdrop-dark: #9a9a9a;
    --brand-blue: #1a8fe0;
    --brand-blue-deep: #0b7fd3;
    --brand-green: #8cc63f;
    --silver-light: #f1f2f4;
    --silver: #c9ccd1;
    --silver-dark: #a7abb2;
    --ink: #111111;
    --ink-soft: #555555;
    --paper: #ffffff;
  }
  * { box-sizing: border-box; margin: 0; padding: 0; }
  html, body { width: 1200px; height: 960px; overflow: hidden; }
  body {
    background: radial-gradient(ellipse at 45% 35%, var(--backdrop-light) 0%, #c4c4c4 55%, var(--backdrop-dark) 100%);
    font-family: "Arimo", Arial, sans-serif;
    position: relative;
  }
  .card {
    position: absolute;
    width: 700px;
    height: 400px;
    left: 250px;
    border-radius: 4px;
    box-shadow: 0 14px 30px rgba(0,0,0,0.28);
    overflow: hidden;
  }
  .card--front {
    top: 50px;
    background: linear-gradient(160deg, #2a9bea 0%, var(--brand-blue) 50%, var(--brand-blue-deep) 100%);
  }
  .card--back {
    top: 510px;
    background: linear-gradient(180deg, var(--paper) 0%, var(--paper) 55%, var(--silver-light) 100%);
  }

  /* front */
  .front-brand {
    position: absolute; left: 120px; top: 80px;
    display: flex; align-items: center; gap: 26px;
  }
  .brand-dot {
    width: 130px; height: 130px; border-radius: 50%;
    background: var(--paper); flex: none;
  }
  .front-brand .brand-name {
    font-family: "Montserrat", Arial, sans-serif; font-weight: 600;
    color: var(--paper); font-size: 46px; line-height: 1.05; letter-spacing: 1px;
  }
  .front-rule {
    position: absolute; left: 120px; right: 120px; top: 268px; height: 2px;
    background: linear-gradient(90deg, var(--silver-dark), var(--silver-light), var(--silver-dark));
  }
  .tagline {
    position: absolute; left: 0; right: 0; top: 288px; text-align: center;
    font-family: "Titillium Web", Arial, sans-serif; font-weight: 600;
    color: var(--brand-green); font-size: 22px; letter-spacing: 0.3px;
  }

  /* back */
  .back-brand {
    position: absolute; left: 50px; top: 40px;
    display: flex; align-items: center; gap: 18px;
  }
  .back-brand .brand-dot { width: 82px; height: 82px; background: var(--brand-blue); }
  .back-brand .brand-name {
    font-family: "Montserrat", Arial, sans-serif; font-weight: 600;
    color: var(--brand-blue); font-size: 24px; line-height: 1.15;
  }
  .divider {
    position: absolute; left: 400px; top: 36px; width: 1px; height: 90px;
    background: var(--silver-dark);
  }
  .person { position: absolute; right: 45px; top: 58px; text-align: right; }
  .person__name { font-size: 34px; font-weight: 700; color: var(--ink); }
  .person__role { font-size: 17px; color: var(--ink-soft); margin-top: 4px; }
  .trim {
    position: absolute; left: 0; right: 0; top: 150px; height: 8px;
    background: linear-gradient(90deg, var(--brand-blue-deep), var(--brand-blue));
  }
  .trim::after {
    content: ""; position: absolute; left: 0; right: 0; top: 10px; height: 3px;
    background: linear-gradient(90deg, var(--silver-dark), var(--silver-light), var(--silver-dark));
  }
  .address {
    position: absolute; left: 50px; top: 188px;
    font-size: 16px; line-height: 1.4; color: var(--ink); font-style: normal;
  }
  .address__company { font-weight: 700; }
  .contacts {
    position: absolute; right: 45px; bottom: 34px;
    list-style: none; text-align: right;
  }
  .contacts li {
    display: flex; align-items: center; justify-content: flex-end; gap: 12px;
    font-size: 17px; color: var(--ink); height: 34px;
  }
  .contact-icon { width: 26px; height: 26px; flex: none; }
  .silver-base {
    position: absolute; left: 0; right: 0; bottom: 0; height: 12px;
    background: linear-gradient(90deg, var(--silver-dark), var(--silver-light) 50%, var(--silver-dark));
  }
</style>
</head>
<body>

  <section class="card card--front" aria-label="Business card front">
    <div class="front-brand">
      <span class="brand-dot"></span>
      <div class="brand-name">Brightpath<br>HR Consulting</div>
    </div>
    <span class="front-rule"></span>
    <p class="tagline">Recruitment | HR Solutions | Business Consultancy</p>
  </section>

  <section class="card card--back" aria-label="Business card back">
    <div class="back-brand">
      <span class="brand-dot"></span>
      <div class="brand-name">Brightpath<br>HR Consulting</div>
    </div>
    <span class="divider"></span>
    <div class="person">
      <div class="person__name">Marcus Tellon</div>
      <div class="person__role">Business Development Director</div>
    </div>
    <span class="trim"></span>
    <address class="address">
      <div class="address__company">Brightpath HR Consulting Pte. Ltd.</div>
      <div>27, Wexford Lane, #05-03B</div>
      <div>Harbourview Trade Tower</div>
      <div>Singapore 061739</div>
    </address>
    <ul class="contacts">
      <li>+65 9438-6157
        <svg class="contact-icon" viewBox="0 0 26 26" aria-hidden="true">
          <circle cx="13" cy="13" r="13" fill="#1a8fe0"/>
          <rect x="9" y="6" width="8" height="14" rx="1.5" fill="none" stroke="#fff" stroke-width="1.6"/>
          <line x1="12" y1="17.5" x2="14" y2="17.5" stroke="#fff" stroke-width="1.4"/>
        </svg>
      </li>
      <li>mtellon@brightpathhr-advisory.com
        <svg class="contact-icon" viewBox="0 0 26 26" aria-hidden="true">
          <circle cx="13" cy="13" r="13" fill="#1a8fe0"/>
          <rect x="7" y="8.5" width="12" height="9" rx="1" fill="#fff"/>
          <polyline points="7,9 13,14 19,9" fill="none" stroke="#1a8fe0" stroke-width="1.4"/>
        </svg>
      </li>
      <li>brightpathhradvisory@mailbox-example.com
        <svg class="contact-icon" viewBox="0 0 26 26" aria-hidden="true">
          <circle cx="13" cy="13" r="13" fill="#1a8fe0"/>
          <rect x="7" y="8.5" width="12" height="9" rx="1" fill="#fff"/>
          <polyline points="7,9 13,14 19,9" fill="none" stroke="#1a8fe0" stroke-width="1.4"/>
        </svg>
      </li>
    </ul>
    <span class="silver-base"></span>
  </section>

</body>
</html>
```